Commercial Real Estate website

Need a web design commercial real estate company specializing in retail shopping centers based in Orlando, FL. We would like pictures of Orlando city skyline with hues and colors that go with hot pink. We want to stress the relationship of time on the value of real estate.
It should gave a rotating page that highlights our property listings.

Target Market(s)

Owners of shopping centers and national retail tenants looking for tenant representatives.

Industry/Entity Type

Real Estate

Number of Pages Required

5+ page

Font styles to use
Serif

Colors
e34197

Requirements
Must have
• Pictures of commercial retail grocery anchored shopping centers and city scapes and skylines.

```html
<!DOCTYPE html>
<html lang="en">
<head>
<meta charset="utf-8">
<title>Keystone Commercial</title>
<link rel="stylesheet" href="https://fonts.googleapis.com/css2?family=Open+Sans:wght@400;600;700&family=Lato:wght@400;700&display=swap">
<style>
:root{
  --pink:#e34197;
  --pink-dark:#c52a7c;
  --pink-soft:#f06ab2;
  --ink:#333;
  --muted:#777;
  --grey-band:#e9e9e9;
  --footer:#2b2b2b;
  --footer-dark:#1e1e1e;
  --white:#fff;
}
*{box-sizing:border-box;margin:0;padding:0}
html,body{width:667px;height:1200px;overflow:hidden;background:var(--white)}
body{font-family:"Open Sans",Arial,sans-serif;color:var(--ink);font-size:7px;line-height:1.45}
.page{width:667px;height:1200px;position:relative}

.site-header{height:67px;display:flex;justify-content:space-between;align-items:center;padding:0 58px}
.brand{display:flex;align-items:center;gap:6px}
.brand-dot{width:14px;height:14px;border-radius:50%;background:var(--pink)}
.brand-name{font-family:"Lato",sans-serif;font-weight:700;font-size:15px;color:var(--pink-dark);line-height:1}
.call{text-align:right}
.call-label{color:var(--pink);font-size:8px}
.call-number{display:flex;align-items:center;gap:4px;font-size:13px;color:var(--ink)}

.main-nav{height:23px;background:var(--pink);display:flex;justify-content:center;gap:34px;align-items:center}
.main-nav a{color:var(--white);text-decoration:none;font-size:7.5px;font-weight:600;text-transform:uppercase}

.hero{position:relative;height:265px;background:linear-gradient(180deg,#e7a0a8 0%,#8a6b86 40%,#2f3b5c 70%,#1b2236 100%);text-align:center;color:var(--white)}
.hero-title{position:absolute;top:92px;width:100%;font-family:"Lato",sans-serif;font-size:22px}
.hero-sub{position:absolute;top:122px;width:100%;font-size:13px}
.btn{display:inline-block;background:var(--pink);color:var(--white);font-size:6px;text-transform:uppercase;padding:4px 10px;font-weight:600}
.hero .btn{position:absolute;top:147px;left:50%;transform:translateX(-50%);font-size:7px;padding:5px 12px}
.dots{position:absolute;bottom:6px;width:100%;display:flex;justify-content:center;gap:4px}
.dots span{width:7px;height:7px;border-radius:50%;background:#bbb}
.dots span:first-child{background:var(--white)}

.welcome{height:110px;text-align:center;padding:14px 80px 0}
.section-title{font-family:"Lato",sans-serif;font-size:15px;color:var(--ink);font-weight:400}
.welcome .rule{width:260px;height:1px;background:var(--pink);margin:4px auto 8px}
.welcome p{color:var(--muted);font-size:6px}

.featured{height:220px;background:linear-gradient(90deg,var(--pink-dark),var(--pink-soft) 50%,var(--pink-dark));position:relative;text-align:center;padding-top:6px}
.featured .section-title{color:var(--white);font-size:18px}
.cards{display:flex;justify-content:center;gap:6px;margin-top:8px}
.card{width:122px;height:145px;background:var(--white);padding:4px}
.card-photo{height:68px;background:linear-gradient(160deg,#9fb7d2,#c9ccd1 60%,#8a8f96)}
.card h3{font-size:9px;font-weight:400;margin-top:5px}
.card p{font-size:5px;color:var(--muted);margin:3px 6px 5px}
.arrow{position:absolute;top:118px;width:14px;height:24px}
.arrow.left{left:28px}.arrow.right{right:28px}

.success{height:200px;display:flex;background:var(--grey-band)}
.success-copy{width:300px;padding:24px 0 0 40px}
.success-copy h2{font-family:"Lato",sans-serif;font-size:17px;font-weight:400}
.success-copy .lead{font-size:6.5px;margin:8px 0 10px}
.success-copy p{font-size:5.5px;color:var(--muted)}
.success-copy a{display:block;color:var(--pink);font-size:6.5px;margin-top:10px}
.success-photo{flex:1;background:linear-gradient(140deg,#3b6fb0,#8ab4dc 45%,#cfd3d8 70%,#9a9fa6);clip-path:polygon(18% 0,100% 0,100% 100%,0 100%)}

.news{height:120px;padding:14px 40px 0}
.news h2{font-family:"Lato",sans-serif;font-size:17px;font-weight:400}
.news-grid{display:flex;gap:30px;margin-top:12px}
.news-item{flex:1}
.news-item h4{color:var(--pink);font-size:6.5px;font-weight:600}
.news-item p{font-size:5.5px;color:var(--muted);margin-top:3px}

.site-footer{height:190px;background:var(--footer);color:#bbb;position:relative;padding:36px 90px 0}
.footer-notch{position:absolute;top:0;left:50%;transform:translateX(-50%)}
.footer-cols{display:flex;justify-content:space-between}
.footer-cols h5{color:var(--white);font-size:6.5px;margin-bottom:6px}
.footer-cols li{list-style:none;font-size:5.5px;line-height:1.8}
.social{display:flex;gap:4px;margin-top:6px}
.social span{width:9px;height:9px;border-radius:50%;background:#777}
.footer-bottom{position:absolute;bottom:0;left:0;right:0;height:28px;background:var(--footer-dark);font-size:5.5px;padding:9px 58px}
</style>
</head>
<body>
<div class="page">
  <header class="site-header">
    <div class="brand"><span class="brand-dot"></span><span class="brand-name">Keystone Commercial</span></div>
    <div class="call">
      <div class="call-label">Call Us Now</div>
      <div class="call-number">
        <svg width="10" height="10" viewBox="0 0 24 24"><path fill="#e34197" d="M6.6 10.8a15 15 0 0 0 6.6 6.6l2.2-2.2a1 1 0 0 1 1-.25 11.4 11.4 0 0 0 3.6.6 1 1 0 0 1 1 1V20a1 1 0 0 1-1 1A17 17 0 0 1 3 4a1 1 0 0 1 1-1h3.5a1 1 0 0 1 1 1c0 1.25.2 2.45.6 3.6a1 1 0 0 1-.25 1z"/></svg>
        407.555.0142
      </div>
    </div>
  </header>

  <nav class="main-nav">
    <a>Home</a><a>About Us</a><a>Properties ▾</a><a>Investors</a><a>Testimonial</a><a>Contact</a>
  </nav>

  <section class="hero" role="img" aria-label="Orlando city skyline at dusk reflected on a lake">
    <div class="hero-title">Pellentesque faucibus accumsan</div>
    <div class="hero-sub">Donec dictum lectus non odio</div>
    <span class="btn">Contact Us</span>
    <div class="dots"><span></span><span></span><span></span><span></span><span></span></div>
  </section>

  <section class="welcome">
    <h2 class="section-title">WELCOME TO KEYSTONE COMMERCIAL</h2>
    <div class="rule"></div>
    <p>Integer magna augue sodales sed auctor et aliquet id nisi. Fusce feugiat nisi vitae est convallis tincidunt. Morbi gravida lorem ut sapien congue, sit amet tempus ex ultricies. Sed fringilla quam eu magna pharetra, vel porta nibh tempor. Curabitur varius ipsum at leo pretium, ac malesuada ligula faucibus. Nam posuere ante non nulla sagittis, id finibus justo volutpat.</p>
  </section>

  <section class="featured">
    <h2 class="section-title">Featured Properties</h2>
    <svg class="arrow left" viewBox="0 0 14 24"><path d="M11 2 3 12l8 10" stroke="#fff" stroke-width="3" fill="none"/></svg>
    <svg class="arrow right" viewBox="0 0 14 24"><path d="M3 2l8 10-8 10" stroke="#fff" stroke-width="3" fill="none"/></svg>
    <div class="cards">
      <article class="card"><div class="card-photo" role="img" aria-label="Grocery anchored shopping center"></div><h3>PropertyTitle</h3><p>Retail plaza with anchor tenant and parking.</p><span class="btn">Read More</span></article>
      <article class="card"><div class="card-photo" role="img" aria-label="Retail storefront building"></div><h3>PropertyTitle</h3><p>Corner retail site with strong street frontage.</p><span class="btn">Read More</span></article>
      <article class="card"><div class="card-photo" role="img" aria-label="Commercial building exterior"></div><h3>PropertyTitle</h3><p>Neighborhood center near major city roads.</p><span class="btn">Read More</span></article>
      <article class="card"><div class="card-photo" role="img" aria-label="Shopping center parking lot"></div><h3>PropertyTitle</h3><p>Community strip mall with open lease space.</p><span class="btn">Read More</span></article>
    </div>
  </section>

  <section class="success">
    <div class="success-copy">
      <h2>Sucess Stories</h2>
      <p class="lead">Mauris vel lacus vitae felis vestibulum volutpat in a massa. Nam dictum tempus sapien in commodo.</p>
      <p>Suspendisse potenti. Vestibulum ante ipsum primis in faucibus orci luctus et ultrices posuere cubilia. Cras viverra sem at tortor malesuada, sed imperdiet dui tempor. Aenean vitae magna nec nisl aliquet rhoncus.</p>
      <a>Read More</a>
    </div>
    <div class="success-photo" role="img" aria-label="Modern blue commercial building under clear sky"></div>
  </section>

  <section class="news">
    <h2>Latest News</h2>
    <div class="news-grid">
      <div class="news-item"><h4>Cras ante nisi porta sit amet</h4><p>Vivamus lacinia odio vitae vestibulum tempor, donec porta nunc a lectus varius. Read more</p></div>
      <div class="news-item"><h4>Aliquam dignissim sem ligula</h4><p>Proin at eros non eros adipiscing mollis, praesent vel erat in urna luctus. Read more</p></div>
      <div class="news-item"><h4>Nullam dignissim congue nisi</h4><p>Etiam iaculis nunc ac metus ultrices, fusce commodo turpis quis dolor. Read more</p></div>
    </div>
  </section>

  <footer class="site-footer">
    <svg class="footer-notch" width="20" height="8" viewBox="0 0 20 8"><path d="M0 0h20L10 8z" fill="#fff"/></svg>
    <div class="footer-cols">
      <div><h5>COMPANY</h5><ul><li>About Us</li><li>What We Do</li><li>Gallery</li><li>Testimonials</li></ul></div>
      <div><h5>SERVICES</h5><ul><li>Property Sale</li><li>Tenant Reps</li><li>Property Mgmt</li><li>Leasing</li></ul></div>
      <div><h5>RESOURCES</h5><ul><li>Investors</li><li>Careers</li><li>FAQ</li><li>Contact</li></ul></div>
      <div><h5>CONTACT US</h5><ul><li>210 Lakeview Ave, Suite 400</li><li>Orlando, FL 32801</li><li>407.555.0142</li><li>hello@keystonecre.com</li></ul>
        <div class="social"><span></span><span></span><span></span><span></span></div></div>
    </div>
    <div class="footer-bottom">© 2014 Keystone Commercial. All rights reserved.</div>
  </footer>
</div>
</body>
</html>
```